Pet Shop Website

website will need to have the following features:
• Photo Galleries of each species (Dogs, Cats, Birds, Fish, Reptiles, Rabbits) in a light box popup
o Each species may have several different categories for example:
 Fish
• Marine fish
• Fresh water
• tropical
• Cichlid
• Information Fact sheets of each species – Downloaded as a pdf which can be either
o Care Sheets
o Training Sheets
• Members Area
o Username (Email Address) & Password login
o New signups
o Exclusive Member Deals
o Newsletter options

The front page must be very simple (for example lumavest.com.au) contain the following:
• Product of the week - which can be purchased online
o Short details
o Cost
• Pet Club Sign up picture
• Animal of the week/month
• Contact Phone Number and addresses of the stores
• A jQuery slideshow (Images could include stores, pets etc…)
The main page MUST keep simple. We do not want it cluttered.

Inner Page
The animals / reptile page will need to have:
• Short description of the species
• Photo Galleries
• A list of what is in stock and the list needs to clearly be sorted by each store (Use of Tabs maybe).
• Facts sheets / Info sheets
The type of website ideas (not the type of look that we are necessary after) is and the sort of content that we want to offer are as follows:

http://www.scalenook.com.au/
http://www.brindlecovepaws.com.au/
http://www.thefurrowden.com.au
http://www.tailtown.net.au

Colour in the new website:
Blue
Red
Grey
Yellow

Original site:

http://www.critterglow.com.au
Updates

Hi Guys,

We had feedback from the client and they would like to see a few dark designs.

Thanks                                   

Reason: We would like to reopen this contest back up for a further week

Target Market(s)

Targeting animal lovers

Industry/Entity Type

Store

Requirements
Should not have
• Alter the logo in anyway

```html
<!DOCTYPE html>
<html lang="en">
<head>
<meta charset="utf-8">
<title>Critter Glow – Pet Superstores</title>
<link href="https://fonts.googleapis.com/css2?family=Ubuntu:wght@500;700&family=Arimo:wght@400;700&family=Abril+Fatface&family=Tinos&display=swap" rel="stylesheet">
<style>
:root{
  --navy:#0d1a8a;
  --navy-dark:#060d5c;
  --yellow:#e8d400;
  --red:#dd0a12;
  --grey-text:#5e5e5e;
  --body-text:#333;
  --page:#f2f2f2;
  --footer:#e6e6e6;
  --line:#c9c9c9;
}
*{margin:0;padding:0;box-sizing:border-box}
html,body{width:1081px;height:1200px;overflow:hidden}
body{position:relative;background:var(--page);font-family:"Arimo",Arial,sans-serif;color:var(--body-text)}
.abs{position:absolute}

/* header */
.brand{left:110px;top:30px;display:flex;align-items:center;gap:10px;font-family:"Ubuntu",sans-serif;font-weight:700;font-size:30px;color:var(--navy)}
.brand-mark{width:22px;height:22px;background:var(--yellow);border-radius:50%}
.phone{left:722px;top:66px;font-family:"Ubuntu",sans-serif;font-weight:500;font-size:22px;color:var(--grey-text);display:flex;align-items:center;gap:8px}

.nav{left:92px;top:115px;width:896px;height:41px;border-radius:21px;background:linear-gradient(var(--navy),var(--navy-dark))}
.nav a{position:absolute;top:0;height:41px;line-height:41px;color:#fff;font-family:"Ubuntu",sans-serif;font-weight:700;font-size:12px;text-decoration:none;text-align:center}
.nav a.active{background:var(--yellow);color:#1a1a1a;top:-10px;height:51px;line-height:70px}
.nav .sep{position:absolute;top:6px;width:1px;height:29px;background:#2b37a8}
.search{position:absolute;right:13px;top:8px;width:194px;height:25px;border-radius:13px;background:#fff;font-size:11px;color:#666;padding:6px 13px}

/* hero */
.hero-photo{left:565px;top:190px;width:430px;height:322px;border-radius:40% 40% 10px 10px;background:radial-gradient(ellipse at 50% 55%,#b9aa97,#e6ddd2 70%,var(--page) 100%);z-index:0}
.hero-intro{left:100px;top:200px;z-index:1}
.hero-intro .kicker{font-family:"Ubuntu",sans-serif;font-weight:700;font-size:26px;color:var(--grey-text)}
.hero-intro .title{font-family:"Ubuntu",sans-serif;font-weight:700;font-size:35px;color:var(--red);margin-top:4px;letter-spacing:-.5px;white-space:nowrap}
.hero-intro .place{font-family:"Ubuntu",sans-serif;font-weight:700;font-size:23px;color:var(--yellow);margin-top:2px}
.hero-intro p{width:415px;font-size:11.5px;line-height:16px;color:#444;margin:16px 0 0 5px}
.steps{left:100px;top:398px}
.pager{left:440px;top:525px;width:162px;height:32px;border-radius:16px;background:#fbfbfb;border:1px solid #d8d8d8;display:flex;align-items:center;justify-content:center;gap:9px}
.pager span{width:10px;height:10px;border-radius:50%;background:#cfcfcf}
.pager .arrow{width:17px;height:17px;background:#fff;border:1px solid #999;display:flex;align-items:center;justify-content:center}

/* products */
.products{left:92px;top:584px;width:896px;height:177px;border-radius:10px;background:linear-gradient(#fff,#dcdcdc);border:1px solid #e0e0e0;display:flex}
.product{flex:1;border-right:1px solid #fff;text-align:center;padding-top:14px}
.product:last-child{border-right:0}
.product .shot{width:170px;height:92px;margin:0 auto;border-radius:8px}
.product .desc{font-size:11.5px;line-height:16px;color:#333;margin-top:14px;letter-spacing:.2px}
.product .price{font-size:11px;font-weight:700;color:var(--red);margin-top:5px}
.shot.dogs{background:linear-gradient(#f3e3c6,#c98a46)}
.shot.gifts{background:linear-gradient(#f1e9df,#c94a3c)}
.shot.mixed{background:linear-gradient(#f3e4cb,#d59a58)}

/* lower */
.kittens{left:97px;top:795px;width:280px;height:280px;border-radius:45% 45% 20% 20%;background:radial-gradient(ellipse at 50% 50%,#d69a5c,#8c7458 55%,var(--page) 80%)}
.welcome{left:400px;top:808px;width:220px}
.welcome h2{font-family:"Abril Fatface",serif;font-weight:400;font-size:29px;color:var(--red);letter-spacing:.5px}
.welcome h3{font-family:"Ubuntu",sans-serif;font-weight:700;font-size:17px;color:#999;margin-top:2px}
.welcome p{font-size:11.5px;line-height:16px;text-align:justify;color:#222;margin-top:14px}
.welcome p+p{margin-top:49px}
.divider{left:643px;top:797px;height:315px;border-left:1px dotted #888}
.contact{left:662px;top:805px;width:300px}
.contact h2{font-family:"Ubuntu",sans-serif;font-weight:700;font-size:22px;color:#444}
.store{margin-top:13px;font-size:11.5px;line-height:16px;color:#222}
.store + .store{margin-top:14px}
.store b{color:var(--red);font-style:italic}
.mascot{left:860px;top:835px;width:118px;height:167px;border-radius:40% 40% 20% 20%;background:linear-gradient(#e3b97c,#b98550)}
.rule{left:657px;top:1015px;width:302px;border-top:1px solid var(--line)}
.follow{left:667px;top:1030px;font-family:"Ubuntu",sans-serif;font-weight:700;font-size:16px;color:#333}
.socials{left:660px;top:1058px;display:flex;gap:16px}
.socials span{width:42px;height:42px;border-radius:50%;background:radial-gradient(circle at 40% 35%,#4d9be0,#1c5aa8)}

/* footer */
.footer{left:0;top:1113px;width:1081px;height:87px;background:var(--footer);text-align:center;font-size:11.5px;color:#333;padding-top:28px;line-height:18px}
.footer .links span{margin:0 12px}
</style>
</head>
<body>

<header>
  <div class="abs brand"><span class="brand-mark"></span>Critter Glow</div>
  <div class="abs phone">Call : (08) 9000 4100
    <svg width="56" height="48" viewBox="0 0 56 48" aria-hidden="true"><path d="M6 6c4-4 9-3 10 1l-3 6c2 6 7 11 13 13l6-3c4 1 5 6 1 10-8 6-30-14-27-27z" fill="#222"/><path d="M36 34c8 10 14 4 10-2s2-10 8-4" fill="none" stroke="#222" stroke-width="1.5"/></svg>
  </div>
  <nav class="abs nav">
    <a class="active" style="left:41px;width:107px">HOME PAGE</a>
    <span class="sep" style="left:167px"></span>
    <a style="left:168px;width:113px">ABOUT US</a>
    <span class="sep" style="left:289px"></span>
    <a style="left:290px;width:116px">PETS</a>
    <span class="sep" style="left:406px"></span>
    <a style="left:407px;width:130px">CONTACT US</a>
    <div class="search">-------Search here-----------
      <svg style="position:absolute;right:10px;top:5px" width="15" height="15" viewBox="0 0 15 15" aria-hidden="true"><circle cx="6" cy="6" r="4.5" fill="none" stroke="#333" stroke-width="2"/><path d="M9.5 9.5l4 4" stroke="#333" stroke-width="2.5"/></svg>
    </div>
  </nav>
</header>

<section>
  <div class="abs hero-photo" role="img" aria-label="Group of pets: dogs, cats, a parrot, a chameleon and a goldfish bowl"></div>
  <div class="abs hero-intro">
    <div class="kicker">Welcome to Critter Glow</div>
    <div class="title">YOUR PET SUPERSTORES</div>
    <div class="place">at Westmere and Fernholm</div>
    <p>Lorem Ipsum is simply dummy text of the printing and typesetting industry. Lorem Ipsum has been the industry's standard dummy text ever since the 1500s,printing and typesetting industry. Lorem Ipsum has been the industry's standard dummy text ever since the 1500s,</p>
  </div>
  <svg class="abs steps" width="230" height="100" viewBox="0 0 230 100" aria-label="Slide steps 1 2 3">
    <path d="M14 30 A40 40 0 1 0 80 25" fill="none" stroke="#e0202c" stroke-width="3"/>
    <path d="M85 15 A42 42 0 1 0 150 28" fill="none" stroke="#c8c8c8" stroke-width="3"/>
    <path d="M150 35 A42 42 0 0 1 222 90" fill="none" stroke="#bdbdbd" stroke-width="4"/>
    <text x="42" y="58" font-family="Tinos,serif" font-size="36" fill="#222">1</text>
    <text x="118" y="56" font-family="Tinos,serif" font-size="36" fill="#222">2</text>
    <text x="176" y="72" font-family="Tinos,serif" font-size="36" fill="#222">3</text>
  </svg>
  <div class="abs pager">
    <span class="arrow"><svg width="7" height="7" viewBox="0 0 7 7"><path d="M5 0L1 3.5 5 7z" fill="#444"/></svg></span>
    <span style="background:#aaa"></span><span></span><span></span><span></span><span></span>
    <span class="arrow"><svg width="7" height="7" viewBox="0 0 7 7"><path d="M2 0l4 3.5L2 7z" fill="#444"/></svg></span>
  </div>
</section>

<section class="abs products">
  <div class="product"><div class="shot dogs" role="img" aria-label="Puppies and kittens sitting together"></div><div class="desc">No extended hours over the Christmas<br>Period Fish Tank Setup</div><div class="price">$1,097.00 AUD</div></div>
  <div class="product"><div class="shot gifts" role="img" aria-label="Puppy in a Santa hat beside gift boxes"></div><div class="desc">No extended hours over the Christmas<br>Period Fish Tank Setup</div><div class="price">$1,097.00 AUD</div></div>
  <div class="product"><div class="shot mixed" role="img" aria-label="Kittens and a dog with food bowls"></div><div class="desc">No extended hours over the Christmas<br>Period Fish Tank Setup</div><div class="price">$1,097.00 AUD</div></div>
  <div class="product"><div class="shot gifts" role="img" aria-label="Puppy in a Santa hat beside gift boxes"></div><div class="desc">No extended hours over the Christmas<br>Period Fish Tank Setup</div><div class="price">$1,097.00 AUD</div></div>
</section>

<section>
  <div class="abs kittens" role="img" aria-label="Two kittens, one tabby and one ginger, playing"></div>
  <div class="abs welcome">
    <h2>WELCOME!</h2>
    <h3>To Our Website</h3>
    <p>Praesent vestibulum molestie lacus. Aeneanum nonummy hendrerit mauris. Phasellus portame. Fusce suscipit varius mium sociis natoquemetun penatibus et magnis dis parturient.</p>
    <p>Montes, nascetur ridiculus mus. Nulla dui. Fusce feugiat malesuada odio morbi nunc odio gravida atem cursus nluctus lorem maecenas tristique.</p>
  </div>
  <div class="abs divider"></div>
  <div class="abs contact">
    <h2>Contact Information</h2>
    <div class="store"><b>Shop 4 / 220 Harbour Rd</b><br>WESTMERE W.A 6190<br>Phone: (08) 9000 4210<br>Fax: (08) 9000 4211</div>
    <div class="store"><b>Unit 2 / 18 Meridian Drive</b><br>FERNHOLM W.A 6195<br>Phone: (08) 9000 4320<br>Fax: (08) 9000 4321</div>
  </div>
  <div class="abs mascot" role="img" aria-label="Dog holding a contact us sign"></div>
  <div class="abs rule"></div>
  <div class="abs follow">Follow Us On:</div>
  <div class="abs socials"><span></span><span></span><span></span></div>
</section>

<footer class="abs footer">
  <div class="links">Home<span>|</span>About Us<span>|</span>Health<span>|</span>Body<span>|</span>Skin<span>|</span>Beauty<span>|</span>Contact Us</div>
  <div>Lumavest &nbsp;&nbsp; Copyright 2011. &nbsp;Privacy Policy &nbsp;| &nbsp;Terms of Use</div>
</footer>

</body>
</html>
```